Professional looking Roller Blind Discount Card that portrays quality at a value for money price!

We need a double sided business card designed as a discount card. Size 90mm wide x 55mm high.We would like it to look professional and portray quality at a value for money price point.I have uploaded a word document with a basic layout with the information we want included on each side of the card. Please put your own thought into the layout.

As per word document attached.

```html
<!DOCTYPE html>
<html lang="en">
<head>
<meta charset="utf-8">
<title>K&amp;L Interiors – Roller Blind Discount Card</title>
<link rel="stylesheet" href="https://fonts.googleapis.com/css2?family=Oswald:wght@600&family=Raleway:wght@300;500;700&family=Cormorant+Garamond:wght@500&display=swap">
<style>
  :root {
    --blue: #29a3dd;
    --grey-dark: #555759;
    --grey-mid: #6d6f71;
    --text-grey: #6a6a6a;
    --white: #ffffff;
    --backdrop: #e6e7e8;
    --photo-a: #b8a48f;
    --photo-b: #c9b07a;
  }
  html, body {
    margin: 0;
    width: 1200px;
    height: 896px;
    overflow: hidden;
    background: var(--backdrop);
  }
  .canvas {
    position: relative;
    width: 1200px;
    height: 896px;
    display: flex;
    align-items: center;
    justify-content: center;
    gap: 40px;
  }
  .card {
    position: relative;
    width: 540px;
    height: 330px;
    background: var(--white);
    overflow: hidden;
    box-shadow: 0 6px 18px rgba(0,0,0,0.18);
    font-family: "Raleway", sans-serif;
  }

  /* Front */
  .headline {
    position: absolute;
    left: 26px;
    top: 16px;
    margin: 0;
    font-family: "Oswald", sans-serif;
    font-weight: 600;
    font-size: 36px;
    letter-spacing: 0.5px;
    color: var(--blue);
  }
  .offer {
    position: absolute;
    left: 26px;
    top: 66px;
    margin: 0;
    font-size: 23px;
    font-weight: 300;
    color: var(--text-grey);
  }
  .offer strong { color: var(--blue); font-weight: 700; }
  .photo-strip {
    position: absolute;
    left: 26px;
    top: 108px;
    display: flex;
    gap: 6px;
  }
  .photo {
    width: 132px;
    height: 104px;
  }
  .photo--window { background: linear-gradient(160deg, #d8d2ca, var(--photo-a) 60%, #7f8c6b); }
  .photo--play { background: linear-gradient(140deg, #e0504a, var(--photo-b) 50%, #3f8fd0); }
  .brand {
    display: flex;
    align-items: center;
    gap: 12px;
    color: var(--blue);
    font-family: "Cormorant Garamond", serif;
    font-weight: 500;
    white-space: nowrap;
  }
  .brand-square {
    background: var(--blue);
    flex: none;
  }
  .brand--front {
    position: absolute;
    left: 26px;
    top: 214px;
    font-size: 52px;
    line-height: 1;
  }
  .brand--front .brand-square { width: 16px; height: 16px; }
  .contact-band {
    position: absolute;
    left: 0;
    right: 0;
    bottom: 0;
    height: 46px;
    background: var(--grey-dark);
    color: var(--white);
    font-size: 19px;
    font-weight: 500;
    display: flex;
    align-items: center;
    padding-left: 150px;
    box-sizing: border-box;
  }
  .contact-band .call { color: var(--blue); margin-right: 7px; }

  /* Back */
  .top-rule {
    position: absolute;
    left: 0; right: 0; top: 0;
    height: 5px;
    background: var(--blue);
  }
  .services {
    position: absolute;
    left: 24px;
    top: 22px;
    margin: 0;
    font-size: 20px;
    font-weight: 500;
    line-height: 1.25;
    color: var(--blue);
  }
  .seal {
    position: absolute;
    right: 26px;
    top: 18px;
    width: 108px;
    height: 108px;
  }
  .seal-title {
    font-family: "Oswald", sans-serif;
    font-weight: 600;
    font-size: 17px;
    fill: var(--white);
    letter-spacing: 0.5px;
  }
  .seal-ribbon-text {
    font-family: "Raleway", sans-serif;
    font-weight: 700;
    font-size: 10.5px;
    fill: var(--white);
    letter-spacing: 0.8px;
  }
  .brand--back {
    position: absolute;
    left: 210px;
    top: 150px;
    font-size: 34px;
  }
  .brand--back .brand-square { width: 14px; height: 14px; }
  .discount {
    position: absolute;
    left: 18px;
    top: 164px;
    width: 150px;
    height: 78px;
  }
  .discount-label {
    position: absolute;
    left: 18px;
    top: 164px;
    width: 130px;
    height: 78px;
    display: flex;
    align-items: center;
    justify-content: center;
    font-family: "Oswald", sans-serif;
    font-weight: 600;
    font-size: 28px;
    color: var(--white);
  }
  .tagline-band {
    position: absolute;
    left: 0; right: 0;
    bottom: 46px;
    height: 32px;
    background: var(--blue);
    color: var(--white);
    font-size: 17px;
    font-weight: 500;
    display: flex;
    align-items: center;
    padding-left: 240px;
    box-sizing: border-box;
  }
  .contact-band--back { padding-left: 240px; }
</style>
</head>
<body>
<main class="canvas">

  <section class="card card--front" aria-label="Card front">
    <h1 class="headline">ROLLER BLINDS</h1>
    <p class="offer"><strong>FREE</strong> in Home Measure &amp; Quote</p>
    <div class="photo-strip">
      <div class="photo photo--window" role="img" aria-label="Photo of a room with roller blinds over a window"></div>
      <div class="photo photo--play" role="img" aria-label="Photo of a child playing in a colourful ball pit"></div>
    </div>
    <div class="brand brand--front"><span class="brand-square"></span>K&amp;L INTERIORS</div>
    <div class="contact-band"><span class="call">Call</span>0400 123 456 Today</div>
  </section>

  <section class="card card--back" aria-label="Card back">
    <div class="top-rule"></div>
    <p class="services">Quality Custom Made Roller Blinds<br>Blockout – Screen – Light Filtering</p>
    <svg class="seal" viewBox="0 0 108 108" role="img" aria-label="Best price guarantee seal">
      <circle cx="54" cy="54" r="52" fill="var(--grey-dark)"/>
      <circle cx="54" cy="54" r="44" fill="none" stroke="#ffffff" stroke-width="1.5"/>
      <text class="seal-title" x="54" y="52" text-anchor="middle">BEST PRICE</text>
      <rect x="4" y="60" width="100" height="18" fill="var(--blue)"/>
      <text class="seal-ribbon-text" x="54" y="73" text-anchor="middle">GUARANTEE</text>
    </svg>
    <div class="brand brand--back"><span class="brand-square"></span>K&amp;L INTERIORS</div>
    <svg class="discount" viewBox="0 0 150 78" aria-hidden="true">
      <polygon points="2,2 118,2 148,39 118,76 2,76" fill="var(--blue)"/>
      <polygon points="6,6 115,6 142,39 115,72 6,72" fill="var(--grey-mid)"/>
    </svg>
    <div class="discount-label">25% OFF</div>
    <div class="tagline-band">Family Owned &amp; Operated</div>
    <div class="contact-band contact-band--back">Call 0400 123 456 Today!</div>
  </section>

</main>
</body>
</html>
```